Luxury Wine Label for New Startup Winery

We need a wine label for our new winery startup. We have worked with a local designer but do not feel the resulting label / logo have the elevation required to present our brand as a luxury wine. Our winery is called "Harrowgate Vineyards" and we are focused on extremely high quality hand crafted artisan and estate wines from the Pacific Northwest.
We would like to see designs that utilize a tree line, or other imagery that represents the "Harrowgate" part of our company name. Another interesting feature could be wood grain.
A logo will be required based on your design so please design with this in mind:
This logo should be consistent with the wine bottle label design, and should be representative of our high end exclusive wine while giving a sense of place (Oregon/ Pacific Northwest.)
I will supply an image of the design we received from our local designer, PLEASE NOTE: in general we do like wood grain and tree line concepts but feel the execution was poorly done.
ATTN: Logo design should be suitable for use on: Bottles (Red wine/rose/white wine), Bussiness cards, vehicle signage, business signage, etc
P.S.:
If you have a design that is not outside the box we are still interested in seeing it.
Label is for a burgundy style bottle with a label height of 3.5 - 4" and a width of 3.5-4"
any label <= 4"x4" and >=3.5"x3.5" will be acceptable:
HOWEVER Width should be greater than or equal to height due to the bottle format
Target Market(s)
Wine enthusiasts with adequate discretionary budgets to afford $100 bottles of wine.
Industry/Entity Type
Wine / Winery
Requirements
Must have
- A sense of luxury, a feel of exclusivity, and a theme consistent with our product and brand name
Nice to have
- Tree line, wood grain or other wood themes. Serif fonts
Should not have
- anything cheesy, off topic, hard to read script fonts or anything that makes the label hard to read from a few feet away or too busy

```html
<!DOCTYPE html>
<html lang="en">
<head>
<meta charset="utf-8">
<title>Harrowgate Vineyards – Syrah Label</title>
<link rel="stylesheet" href="https://fonts.googleapis.com/css2?family=Cinzel:wght@400;500&family=Roboto+Slab:wght@500;600&display=swap">
<style>
  :root {
    --page: #ffffff;
    --black: #111111;
    --white: #ffffff;
    --gold: #c9a43a;
    --gold-light: #f1e08f;
    --gold-dark: #b8902a;
    --silver-dark: #6e6e6e;
    --silver-light: #f4f4f4;
    --wood-dark: #3b2a1d;
    --wood-mid: #6a4c34;
    --ink: #2a2115;
  }
  * { box-sizing: border-box; margin: 0; padding: 0; }
  html, body { width: 1121px; height: 1200px; overflow: hidden; background: var(--page); }
  .canvas { position: relative; width: 1121px; height: 1200px; }

  .front-label { position: absolute; left: 17px; top: 17px; width: 1087px; height: 881px; background: var(--black); }
  .silver-band {
    position: absolute; left: 0; width: 100%;
    background: linear-gradient(90deg, var(--silver-dark) 0%, var(--silver-light) 30%, var(--silver-light) 70%, var(--silver-dark) 100%);
  }
  .silver-band.top { top: 0; height: 65px; }
  .silver-band.bottom { bottom: 0; height: 68px; }
  .gold-stripe { position: absolute; left: 0; width: 100%; height: 14px; background: linear-gradient(90deg, var(--gold-dark), var(--gold), var(--gold-dark)); }
  .gold-stripe.one { top: 763px; }
  .gold-stripe.two { top: 791px; }

  .brand-mark { position: absolute; left: 355px; top: 65px; width: 376px; height: 376px; }
  .brand-mark-name {
    position: absolute; inset: 0; display: flex; align-items: center; justify-content: center;
    font-family: "Cinzel", serif; font-weight: 400; font-size: 34px; letter-spacing: 3px; color: var(--white);
  }

  .brand-name, .brand-sub, .region, .varietal, .vintage-line {
    position: absolute; left: 0; width: 100%; text-align: center; white-space: nowrap;
  }
  .brand-name { top: 510px; font-family: "Cinzel", serif; font-weight: 500; font-size: 70px; letter-spacing: 4px; color: var(--white); line-height: 1; }
  .brand-sub { top: 590px; font-family: "Cinzel", serif; font-weight: 400; font-size: 50px; letter-spacing: 7px; color: var(--white); line-height: 1; }
  .region { top: 680px; font-family: "Roboto Slab", serif; font-weight: 500; font-size: 37px; letter-spacing: 3px; color: var(--gold); line-height: 1; }

  .back-label { position: absolute; left: 17px; top: 941px; width: 1087px; height: 240px; }
  .gold-band {
    position: absolute; left: 0; width: 100%; height: 38px;
    background: linear-gradient(90deg, var(--gold) 0%, var(--gold-light) 45%, var(--gold-light) 60%, var(--gold) 100%);
  }
  .gold-band.top { top: 0; }
  .gold-band.bottom { bottom: 0; }
  .wood-panel {
    position: absolute; left: 0; top: 38px; width: 100%; height: 164px;
    background: linear-gradient(180deg, var(--wood-mid) 0%, var(--wood-dark) 45%, var(--wood-mid) 100%);
  }
  .varietal { top: 82px; font-family: "Cinzel", serif; font-weight: 400; font-size: 84px; letter-spacing: 5px; color: var(--white); line-height: 1; }
  .vintage-line { top: 211px; font-family: "Roboto Slab", serif; font-weight: 600; font-size: 20px; letter-spacing: 3px; color: var(--ink); line-height: 1; }
</style>
</head>
<body>
<main class="canvas">
  <section class="front-label">
    <div class="silver-band top"></div>

    <div class="brand-mark">
      <svg width="376" height="376" viewBox="0 0 376 376" aria-hidden="true">
        <circle cx="188" cy="188" r="178" fill="none" stroke="var(--white)" stroke-width="16"/>
      </svg>
      <span class="brand-mark-name">Harrowgate</span>
    </div>

    <h1 class="brand-name">HARROWGATE</h1>
    <p class="brand-sub">VINEYARDS</p>
    <p class="region">“WILLAMETTE VALLEY”</p>

    <div class="gold-stripe one"></div>
    <div class="gold-stripe two"></div>
    <div class="silver-band bottom"></div>
  </section>

  <section class="back-label">
    <div class="gold-band top"></div>
    <div class="wood-panel" role="img" aria-label="Dark walnut wood grain texture"></div>
    <h2 class="varietal">SYRAH</h2>
    <div class="gold-band bottom"></div>
    <p class="vintage-line">ESTATE | 2023 | GROWN</p>
  </section>
</main>
</body>
</html>
```